Flyer for a marketing

We are a holistic mental health facility in need of a flyer to help promote our services and encourage more people to seek care. See the attachment to tell you more. We prefer warm green colors or rich blue. Thank you.

```html
<!DOCTYPE html>
<html lang="en">
<head>
<meta charset="utf-8">
<title>Evenfield Mind Clinic – Flyer</title>
<link rel="stylesheet" href="https://fonts.googleapis.com/css2?family=Merriweather:wght@400;700&family=Montserrat:wght@400&display=swap">
<style>
  :root{
    --page:#e7e4dd;
    --sky:#2cc0ef;
    --sky-light:#5ccdf4;
    --royal:#2650a3;
    --ribbon:#2a4ea6;
    --navy:#1c3566;
    --ink:#1b2f63;
    --white:#ffffff;
    --serif:'Merriweather', Georgia, serif;
    --sans:'Montserrat', Arial, sans-serif;
  }
  *{margin:0;padding:0;box-sizing:border-box}
  html,body{width:1200px;height:1117px;overflow:hidden;background:var(--page)}
  .flyer{position:absolute;left:219px;top:20px;width:761px;height:1077px;overflow:hidden;background:var(--white);font-family:var(--serif);box-shadow:0 4px 14px rgba(0,0,0,.18)}
  .flyer-bg{position:absolute;inset:0}
  .abs{position:absolute}
  .brand{left:160px;top:100px;display:flex;align-items:center;gap:18px}
  .brand-dot{width:54px;height:54px;border-radius:50%;background:var(--sky);flex:none}
  .brand-name{font-weight:700;font-size:34px;line-height:44px;color:var(--ink);white-space:nowrap}
  .tagline{left:120px;width:672px;top:200px;text-align:center;font-family:var(--sans);font-size:28px;letter-spacing:1px;color:var(--ink)}
  .intro{left:0;width:761px;top:300px;text-align:center;font-weight:700;font-size:19px;line-height:23px;color:var(--white)}
  .headline{left:0;width:761px;top:588px;text-align:center;font-weight:700;font-size:34px;line-height:40px;color:var(--white)}
  .headline-sub{left:0;width:761px;top:672px;text-align:center;font-weight:700;font-size:12.5px;color:var(--white)}
  .why-pill{left:155px;top:711px;width:450px;height:37px;border-radius:4px;background:var(--sky);color:var(--white);font-weight:700;font-size:26px;line-height:37px;text-align:center}
  .why-list{left:0;width:761px;top:759px;list-style:none;text-align:center;font-weight:700;font-size:14px;line-height:21px;color:var(--ink)}
  .ribbon-title{left:84px;top:905px;font-weight:400;font-size:20px;line-height:32px;color:var(--white)}
  .contact{font-size:17px;line-height:20px;color:var(--white);display:flex;align-items:center;gap:8px;white-space:nowrap}
  .contact svg{width:17px;height:17px;flex:none}
  .contact-divider{left:304px;top:965px;width:2px;height:52px;background:var(--white)}
</style>
</head>
<body>
<div class="flyer">
  <svg class="flyer-bg" width="761" height="1077" viewBox="0 0 761 1077">
    <defs>
      <linearGradient id="skyBand" x1="0" y1="0" x2="0.3" y2="1">
        <stop offset="0" stop-color="#5ccdf4"/>
        <stop offset="1" stop-color="#28b6ea"/>
      </linearGradient>
      <linearGradient id="therapyPhoto" x1="0" y1="0" x2="1" y2="1">
        <stop offset="0" stop-color="#e9e4df"/>
        <stop offset="0.5" stop-color="#c9c4c4"/>
        <stop offset="1" stop-color="#2b3350"/>
      </linearGradient>
      <linearGradient id="familyPhoto" x1="0" y1="0" x2="1" y2="1">
        <stop offset="0" stop-color="#d9d5cf"/>
        <stop offset="0.5" stop-color="#6a7fa8"/>
        <stop offset="1" stop-color="#4a3328"/>
      </linearGradient>
    </defs>
    <rect x="0" y="0" width="761" height="367" fill="url(#skyBand)"/>
    <path d="M86 0 L152 236 Q162 262 198 264 L761 289 V0 Z" fill="#ffffff"/>
    <rect x="0" y="367" width="381" height="211" fill="url(#therapyPhoto)" role="img" aria-label="Photo: a distressed woman talking with a therapist in an office"/>
    <rect x="381" y="367" width="380" height="211" fill="url(#familyPhoto)" role="img" aria-label="Photo: a smiling family of three hugging"/>
    <rect x="0" y="578" width="761" height="499" fill="#2650a3"/>
    <path d="M761 714 L118 740 Q70 744 58 792 L0 1000 V1077 H761 Z" fill="#ffffff"/>
    <path d="M110 880 H761 V1077 H34 L70 912 Q78 880 110 880 Z" fill="#1c3566"/>
    <path d="M48 930 L48 960 Q48 972 60 972 L60 940 Z" fill="#1e3f8f"/>
    <rect x="48" y="902" width="524" height="38" rx="8" fill="#2a4ea6"/>
  </svg>

  <div class="abs brand">
    <span class="brand-dot"></span>
    <span class="brand-name">Evenfield Mind Clinic</span>
  </div>
  <div class="abs tagline">Care That Listens</div>

  <p class="abs intro">Evenfield Mind Clinic, where deserving<br>patients meet compassionate providers.</p>

  <h1 class="abs headline">We are accepting new patients,<br>no waiting list.</h1>
  <p class="abs headline-sub">Your mental health matters, so make it a priority and call us today for an appointment.</p>

  <h2 class="abs why-pill">Why choose us?</h2>
  <ul class="abs why-list">
    <li>We are an integrative holistic psychiatric center.</li>
    <li>Our mission is to provide compassionate quality care.</li>
    <li>We provide psychiatric services including medication management and psychotherapy.</li>
    <li>We listen, care, and empower you to live better.</li>
    <li>We accept major insurances.</li>
  </ul>

  <div class="abs ribbon-title">Evenfield Mind Clinic, APNC</div>

  <div class="abs contact" style="left:98px;top:964px">
    <svg viewBox="0 0 20 20"><circle cx="10" cy="10" r="10" fill="var(--sky)"/><path d="M6.5 5 L8.5 5 L9.3 7.6 L8 8.6 Q9 11 11.4 12 L12.4 10.7 L15 11.5 L15 13.5 Q14.5 15 12.8 14.8 Q6 13.8 5.2 7 Q5 5.5 6.5 5 Z" fill="var(--navy)"/></svg>
    <span>Ph (555) 014-2783</span>
  </div>
  <div class="abs contact" style="left:98px;top:995px">
    <svg viewBox="0 0 20 20"><circle cx="10" cy="10" r="10" fill="var(--sky)"/><rect x="7" y="4.5" width="6" height="4" fill="var(--navy)"/><rect x="5" y="8" width="10" height="5" rx="1" fill="var(--navy)"/><rect x="7" y="11.5" width="6" height="4" fill="var(--navy)"/></svg>
    <span>Fax (555) 019-4410</span>
  </div>
  <div class="abs contact" style="left:98px;top:1027px">
    <svg viewBox="0 0 20 20"><path d="M10 1 C6 1 4 4 4 7 C4 11 10 19 10 19 C10 19 16 11 16 7 C16 4 14 1 10 1 Z" fill="var(--sky)"/><circle cx="10" cy="7" r="2.3" fill="var(--navy)"/></svg>
    <span>4180 Larkspur Avenue, Suite 210 Fairbrook, CA 91500</span>
  </div>

  <div class="abs contact-divider"></div>

  <div class="abs contact" style="left:332px;top:963px">
    <svg viewBox="0 0 20 20"><circle cx="10" cy="10" r="10" fill="var(--sky)"/><rect x="5" y="6.5" width="10" height="7" fill="none" stroke="var(--navy)" stroke-width="1.3"/><path d="M5 6.5 L10 10.5 L15 6.5" fill="none" stroke="var(--navy)" stroke-width="1.3"/></svg>
    <span>info@evenfieldhealth.com</span>
  </div>
  <div class="abs contact" style="left:332px;top:994px">
    <svg viewBox="0 0 20 20"><circle cx="10" cy="10" r="10" fill="var(--sky)"/><circle cx="10" cy="10" r="5.5" fill="none" stroke="var(--navy)" stroke-width="1.2"/><ellipse cx="10" cy="10" rx="2.3" ry="5.5" fill="none" stroke="var(--navy)" stroke-width="1.1"/><path d="M4.5 10 H15.5" stroke="var(--navy)" stroke-width="1.1"/></svg>
    <span>evenfieldhealth.com</span>
  </div>
</div>
</body>
</html>
```